Frostwyn.co - Polar Expeditions Specialists

We need a modern, visually striking business card for Frostwyn.co, a company specialized in selling expedition cruises to the most remote regions on Earth, with a focus on the Arctic and Antarctica. The design should instantly communicate that the cardholder is an expert in polar travel. Use clean, premium aesthetics with cool tones like icy blue and white, possibly incorporating polar imagery (ice, glaciers, penguins, etc.)

Attached the logo

Contact Information for Business Card

Feels high-end and trustworthy.. Visually memorable — encourages people to keep it

Colors
0054AA
0677BA
7BADD7
CADEEF
E8F1F8

Requirements
Must have
• ice, glaciers, penguins, montains
Nice to have
• modern, transparente,

```html
<!DOCTYPE html>
<html lang="en">
<head>
<meta charset="utf-8">
<title>Frostwyn.co Business Card</title>
<link href="https://fonts.googleapis.com/css2?family=Poppins:wght@400;500;600;700&display=swap" rel="stylesheet">
<style>
  :root {
    --page-bg: #ddedfc;
    --ink: #ffffff;
    --sky: #5e9dd9;
    --sky-deep: #3f86cc;
    --ridge: #4f84c2;
    --snow: #9fc2e5;
    --snow-light: #b8d3ee;
    --icon-cut: #5a8fcf;
    --shadow: rgba(0, 0, 0, 0.85);
  }
  * { margin: 0; padding: 0; box-sizing: border-box; }
  html, body {
    width: 1093px; height: 1200px; overflow: hidden;
    background: var(--page-bg);
    font-family: "Poppins", sans-serif;
    color: var(--ink);
  }
  .canvas { position: relative; width: 1093px; height: 1200px; }
  .card {
    position: absolute; left: 265px; height: 357px;
    overflow: hidden;
    box-shadow: 3px 3px 0 var(--shadow);
  }
  .card--back { top: 226px; width: 578px; }
  .card--front { top: 621px; width: 582px; }
  .card__scene {
    position: absolute; inset: 0;
    background:
      linear-gradient(180deg, rgba(255,255,255,0) 55%, rgba(214,232,248,0.45) 85%, rgba(214,232,248,0.5) 100%),
      linear-gradient(165deg, var(--sky-deep) 0%, var(--sky) 28%, var(--ridge) 45%, var(--snow) 70%, var(--snow-light) 100%);
  }
  .t { position: absolute; white-space: nowrap; line-height: 1; }

  .mark-dot { position: absolute; border-radius: 50%; background: var(--ink); }
  .brand { font-weight: 600; letter-spacing: -0.3px; }
  .tagline { font-weight: 500; }

  .card--back .mark-dot { left: 115px; top: 56px; width: 50px; height: 50px; }
  .card--back .brand { left: 0; width: 284px; text-align: center; top: 121px; font-size: 40px; }
  .card--back .tagline { left: 0; width: 284px; text-align: center; top: 167px; font-size: 11px; }

  .person__name { left: 286px; top: 78px; font-size: 25px; font-weight: 600; }
  .person__role { left: 286px; top: 102px; font-size: 17.5px; font-weight: 400; }
  .rule { position: absolute; left: 288px; width: 50px; height: 1px; background: var(--ink); }
  .rule--top { top: 129px; }
  .rule--bottom { top: 214px; }
  .contact {
    position: absolute; left: 286px; display: flex; align-items: center; gap: 7px;
    font-size: 17px; line-height: 1; white-space: nowrap;
  }
  .contact svg { width: 15px; height: 15px; flex: none; }
  .contact--phone { top: 146px; }
  .contact--mail { top: 167px; }
  .contact--web { top: 188px; }
  .address { left: 287px; font-size: 17px; }
  .address--1 { top: 227px; }
  .address--2 { top: 248px; }

  .card--front .mark-dot { left: 253px; top: 57px; width: 72px; height: 72px; }
  .card--front .brand { left: 0; width: 582px; text-align: center; top: 160px; font-size: 55px; }
  .card--front .tagline { left: 0; width: 582px; text-align: center; top: 225px; font-size: 17px; }
</style>
</head>
<body>
<main class="canvas">

  <section class="card card--back">
    <div class="card__scene" role="img" aria-label="Blue-tinted photo of snowy Antarctic mountains and glacier with a line of emperor penguins and chicks"></div>
    <span class="mark-dot" aria-hidden="true"></span>
    <p class="t brand">Frostwyn.co</p>
    <p class="t tagline">Polar Expeditions Specialists</p>

    <h1 class="t person__name">Elias Marrow</h1>
    <p class="t person__role">Managing Director</p>
    <span class="rule rule--top"></span>
    <p class="contact contact--phone">
      <svg viewBox="0 0 24 24" fill="none" stroke="#fff" stroke-width="2"><path d="M5 3h4l2 5-3 2a12 12 0 0 0 6 6l2-3 5 2v4a2 2 0 0 1-2 2A17 17 0 0 1 3 5a2 2 0 0 1 2-2z"/></svg>
      041-582 730 164
    </p>
    <p class="contact contact--mail">
      <svg viewBox="0 0 24 24" fill="#fff"><path d="M2 5h20v14H2z"/><path d="M2 5l10 8 10-8" stroke="#5a8fcf" stroke-width="1.6" fill="none"/></svg>
      hello@frostwyn.co
    </p>
    <p class="contact contact--web">
      <svg viewBox="0 0 24 24" fill="none" stroke="#fff" stroke-width="1.8"><circle cx="12" cy="12" r="10"/><ellipse cx="12" cy="12" rx="4" ry="10"/><path d="M2 12h20M4 7h16M4 17h16"/></svg>
      www.frostwyn.co
    </p>
    <span class="rule rule--bottom"></span>
    <p class="t address address--1">18, Glacier Quay Road</p>
    <p class="t address address--2">70314, Norland</p>
  </section>

  <section class="card card--front">
    <div class="card__scene" role="img" aria-label="Blue-tinted photo of Antarctic peaks, cloudy sky and a column of emperor penguins on the snow"></div>
    <span class="mark-dot" aria-hidden="true"></span>
    <p class="t brand">Frostwyn.co</p>
    <p class="t tagline">Polar Expeditions Specialists</p>
  </section>

</main>
</body>
</html>
```